Vantor Brochure Design Project

Brochure for Exclusive Concierge Service In St. Kitts.
Company Nam Vantor St. Kitts
Colours should be Black and Copper

Target Market(s)

Very high end exclusive market

Industry/Entity Type

It Company

Requirements
Must have
• Also must have Flag of the Country St. Kitts and Nevis
Nice to have
• I like a circular design, with unique cut out

```html
<!DOCTYPE html>
<html lang="en">
<head>
<meta charset="utf-8">
<title>Vantor St. Kitts – Brochure Back Panel</title>
<link rel="stylesheet" href="https://fonts.googleapis.com/css2?family=Alegreya:wght@400&family=Alegreya+SC:wght@400&display=swap">
<style>
  :root {
    --backdrop: #d3d8d8;
    --paper: #ffffff;
    --ink: #2b2b2b;
    --copper: #c27a52;
    --flag-green: #2fb34a;
    --flag-red: #e3242b;
    --flag-yellow: #f7e11a;
    --flag-black: #111111;
  }
  * { margin: 0; padding: 0; box-sizing: border-box; }
  html, body {
    width: 1200px;
    height: 900px;
    overflow: hidden;
    background: var(--backdrop);
  }
  .brochure {
    position: relative;
    width: 1200px;
    height: 900px;
    font-family: "Alegreya", Georgia, serif;
    color: var(--ink);
  }
  .brochure__sheet {
    position: absolute;
    inset: 0;
  }
  .brochure__tagline {
    font-family: "Alegreya", Georgia, serif;
    font-size: 21px;
    fill: var(--ink);
    letter-spacing: 0.2px;
  }
  .brochure__content {
    position: absolute;
    left: 0;
    right: 0;
    top: 270px;
    text-align: center;
  }
  .flag {
    display: block;
    margin: 0 auto 26px;
    width: 120px;
    height: 80px;
  }
  .address {
    font-style: normal;
    font-size: 23px;
    line-height: 1.15;
    margin-bottom: 34px;
  }
  .contact {
    list-style: none;
    font-size: 21px;
    line-height: 1.2;
  }
  .contact__label {
    font-family: "Alegreya SC", Georgia, serif;
  }
</style>
</head>
<body>
<main class="brochure">
  <svg class="brochure__sheet" width="1200" height="900" viewBox="0 0 1200 900" aria-hidden="false">
    <defs>
      <path id="tagline-arc" d="M80 340 A735 735 0 0 1 1120 340" fill="none"/>
    </defs>
    <!-- fan-shaped panel -->
    <path class="sheet__panel" d="M600 860 L63 323 A760 760 0 0 1 1137 323 Z" fill="var(--paper)"/>
    <!-- copper edge trim -->
    <line class="sheet__trim" x1="604" y1="856" x2="1130" y2="330" stroke="var(--copper)" stroke-width="7"/>
    <!-- dotted arc -->
    <path class="sheet__dotted-arc" d="M97 357 A712 712 0 0 1 1103 357" fill="none" stroke="var(--copper)" stroke-width="3.2" stroke-linecap="round" stroke-dasharray="0 7"/>
    <text class="brochure__tagline">
      <textPath href="#tagline-arc" startOffset="50%" text-anchor="middle">We are the Hospitality Ambassadors for the Caribbean’s best location, St. Kitts and Nevis-Two Islands, One Paradise!</textPath>
    </text>
  </svg>

  <section class="brochure__content">
    <svg class="flag" viewBox="0 0 120 80" role="img" aria-label="Flag of St. Kitts and Nevis">
      <polygon points="0,0 120,0 0,80" fill="var(--flag-green)"/>
      <polygon points="120,0 120,80 0,80" fill="var(--flag-red)"/>
      <polygon points="0,62 93,0 120,0 120,18 27,80 0,80" fill="var(--flag-yellow)"/>
      <polygon points="0,71 106,0 120,0 120,9 14,80 0,80" fill="var(--flag-black)"/>
      <polygon points="42,46 43.9,50.3 48.5,50.6 45,53.5 46.1,58 42,55.5 37.9,58 39,53.5 35.5,50.6 40.1,50.3" fill="#fff"/>
      <polygon points="80,22 81.9,26.3 86.5,26.6 83,29.5 84.1,34 80,31.5 75.9,34 77,29.5 73.5,26.6 78.1,26.3" fill="#fff"/>
    </svg>

    <address class="address">
      P.O. Box 2048<br>
      Cnr. of Bay &amp; Market Street<br>
      Basseterre, St. Kitts<br>
      St. Kitts
    </address>

    <ul class="contact">
      <li><span class="contact__label">Phone</span> • 869-555-0142</li>
      <li><span class="contact__label">Fax</span> • 869-555-0187</li>
      <li><span class="contact__label">E-mail</span> • info@vantorstkitts.com</li>
      <li><span class="contact__label">Website</span> • www.vantorstkitts.com</li>
    </ul>
  </section>
</main>
</body>
</html>
```